Bref créative
TRVB Business cards and stationary
TRVB business cards
Use same font as used in my logo
Marcus Delaney
President
487 W. Harborview Lane
Suite 318
Coral Springs, FL 33065
marcus@tuitionreliefvb.com
www.TuitionReliefVB.com

```html
<!DOCTYPE html>
<html lang="en">
<head>
<meta charset="utf-8">
<title>TRVB Stationery</title>
<link href="https://fonts.googleapis.com/css2?family=Cinzel:wght@400;600&family=Open+Sans:wght@400;600&display=swap" rel="stylesheet">
<style>
:root{
  --bg:#eceef0;
  --paper:#ffffff;
  --red:#b3121b;
  --red-dark:#8c0d14;
  --ink:#5a5a5a;
  --muted:#9a9a9a;
  --line:#e3e3e3;
}
*{margin:0;padding:0;box-sizing:border-box}
html,body{width:1200px;height:936px;overflow:hidden;background:var(--bg)}
body{position:relative;font-family:"Open Sans",Arial,sans-serif;color:var(--ink)}
.sheet{position:absolute;background:var(--paper);box-shadow:0 4px 10px rgba(0,0,0,.12);overflow:hidden}
.brand{display:flex;align-items:center;gap:6px;font-family:"Cinzel",Georgia,serif;font-weight:600;color:var(--red);white-space:nowrap;line-height:1}
.brand .dot{border-radius:50%;background:var(--red);flex:none}
.band{position:absolute;left:0;right:0;background:linear-gradient(var(--red),var(--red-dark));color:#fff;text-align:center;letter-spacing:3px;font-size:7px;display:flex;align-items:center;justify-content:center}

/* letterhead */
.letterhead{left:152px;top:71px;width:419px;height:538px}
.letterhead .brand{position:absolute;left:46px;top:34px;font-size:13px}
.letterhead .brand .dot{width:9px;height:9px}
.contact{position:absolute;left:312px;top:32px;list-style:none;font-size:5.5px;color:var(--muted);line-height:9px}
.contact li{display:flex;align-items:center;gap:4px;white-space:nowrap}
.contact li::before{content:"";width:5px;height:5px;background:var(--red);flex:none}
.letterhead .band{bottom:0;height:20px}

/* folder */
.folder{left:634px;top:71px;width:416px;height:538px}
.folder .brand{position:absolute;left:50%;top:258px;transform:translateX(-50%);font-size:30px;gap:10px}
.folder .brand .dot{width:20px;height:20px}
.folder .rule{position:absolute;left:0;right:0;bottom:22px;height:2px;background:var(--red)}
.folder .band{bottom:0;height:18px}

/* business cards */
.card{width:195px;height:108px}
.card-front{left:46px;top:680px}
.card-front .brand{position:absolute;left:9px;top:24px;font-size:6px;gap:3px}
.card-front .brand .dot{width:5px;height:5px}
.card-front .panel{position:absolute;right:0;top:0;width:100px;height:100%;background:linear-gradient(var(--red),var(--red-dark));color:#fff;padding:18px 6px 0 9px;font-size:4.8px;line-height:8px;white-space:nowrap}
.card-front .panel .name{font-size:6.5px;font-weight:600}
.card-back{left:46px;top:802px;height:106px}
.card-back .brand{position:absolute;left:14px;top:30px;font-size:9px;gap:4px}
.card-back .brand .dot{width:7px;height:7px}
.card-back .web{position:absolute;left:14px;bottom:14px;font-size:4.5px;color:var(--muted);letter-spacing:1px}

/* envelopes */
.envelope-front{left:266px;top:680px;width:363px;height:198px}
.envelope-front .brand{position:absolute;left:14px;top:18px;font-size:10px;gap:4px}
.envelope-front .brand .dot{width:7px;height:7px}
.envelope-front .return{position:absolute;left:14px;top:36px;font-size:5px;line-height:7px;color:var(--muted)}
.envelope-front .band{bottom:0;height:18px}
.envelope-back{left:660px;top:680px;width:390px;height:198px}
.envelope-back svg{position:absolute;left:0;top:0}
.envelope-back .web{position:absolute;left:0;right:0;top:18px;text-align:center;color:#fff;font-size:7px;letter-spacing:3px}
</style>
</head>
<body>

<section class="sheet letterhead" aria-label="Letterhead">
  <div class="brand"><span class="dot"></span>Tuition Relief VB</div>
  <ul class="contact">
    <li>487 W. Harborview Lane</li>
    <li>Suite 318</li>
    <li>Coral Springs, FL 33065</li>
    <li>(954) 555-0142</li>
    <li>marcus@tuitionreliefvb.com</li>
  </ul>
  <div class="band">www.TuitionReliefVB.com</div>
</section>

<section class="sheet folder" aria-label="Presentation folder">
  <div class="brand"><span class="dot"></span>Tuition Relief VB</div>
  <div class="rule"></div>
  <div class="band">www.TuitionReliefVB.com</div>
</section>

<section class="sheet card card-front" aria-label="Business card front">
  <div class="brand"><span class="dot"></span>Tuition Relief VB</div>
  <div class="panel">
    <div class="name">Marcus Delaney</div>
    <div>President</div>
    <div>487 W. Harborview Lane</div>
    <div>Suite 318, Coral Springs, FL 33065</div>
    <div>marcus@tuitionreliefvb.com</div>
  </div>
</section>

<section class="sheet card card-back" aria-label="Business card back">
  <div class="brand"><span class="dot"></span>Tuition Relief VB</div>
  <div class="web">www.TuitionReliefVB.com</div>
</section>

<section class="sheet envelope-front" aria-label="Envelope front">
  <div class="brand"><span class="dot"></span>Tuition Relief VB</div>
  <div class="return">487 W. Harborview Lane<br>Suite 318<br>Coral Springs, FL 33065</div>
  <div class="band">www.TuitionReliefVB.com</div>
</section>

<section class="sheet envelope-back" aria-label="Envelope back">
  <svg width="390" height="198" viewBox="0 0 390 198">
    <defs>
      <linearGradient id="flap" x1="0" y1="0" x2="0" y2="1">
        <stop offset="0" stop-color="#b3121b"/>
        <stop offset="1" stop-color="#8c0d14"/>
      </linearGradient>
    </defs>
    <line x1="0" y1="198" x2="175" y2="100" stroke="#e3e3e3"/>
    <line x1="390" y1="198" x2="215" y2="100" stroke="#e3e3e3"/>
    <polygon points="0,0 390,0 390,40 195,92 0,40" fill="url(#flap)"/>
  </svg>
  <div class="web">www.TuitionReliefVB.com</div>
</section>

</body>
</html>
```